Tax Preparation flyer for LedgerMint Corp.

My Client would like a one page PDF flyer to promote upcoming tax season in Canada. This firm is affordable and all virtual. I have attached a copy of their logo and a word document with the proposed wording for the flyer. Please feel free to change if you have better suggestions.

Target Market(s)

individuals in canada

Colors
0054AA
0677BA
7BADD7
CADEEF
E8F1F8

```html
<!DOCTYPE html>
<html lang="en">
<head>
<meta charset="utf-8">
<title>LedgerMint Corp. — Tax Season Flyer</title>
<link href="https://fonts.googleapis.com/css2?family=Poppins:wght@400;500;600;700;800&family=Oswald:wght@500;600&display=swap" rel="stylesheet">
<style>
:root{
  --navy:#0054AA;
  --blue:#0677BA;
  --bright:#1b95d6;
  --sky:#7BADD7;
  --pale:#CADEEF;
  --mist:#E8F1F8;
  --ink:#1f1f21;
  --band:#3a3b3d;
  --stage:#eef0f2;
  --cell:#d9dadc;
}
*{margin:0;padding:0;box-sizing:border-box}
html,body{width:1200px;height:2317px;overflow:hidden;background:var(--stage)}
body{position:relative;font-family:"Poppins",sans-serif;color:var(--ink)}
.flyer{position:absolute;left:0;top:381px;width:979px;height:1268px;background:#fff;transform:scale(1.2257);transform-origin:0 0;overflow:hidden}
.abs{position:absolute}
.hero-art{position:absolute;left:0;top:0;width:979px;height:530px}
.brand{left:55px;top:52px;font-family:"Poppins",sans-serif;font-weight:700;font-size:40px;line-height:44px;color:var(--ink);display:flex;align-items:center;gap:12px}
.brand-dot{width:18px;height:18px;background:var(--bright)}
.headline-relax{left:52px;top:158px;font-weight:800;font-size:88px;line-height:92px;color:var(--bright);letter-spacing:1px}
.headline-sub{left:55px;top:246px;font-size:37px;line-height:40px;font-weight:400}
.headline-main{left:55px;top:282px;font-family:"Oswald",sans-serif;font-weight:600;font-size:62px;line-height:66px;letter-spacing:-1px}
.dash{left:55px;top:359px;width:34px;height:5px;background:var(--bright)}
.intro{left:55px;top:382px;width:380px;font-size:14.6px;line-height:17.5px}
.intro strong{font-weight:700}
.sign-tag{display:inline-flex;align-items:center;gap:4px;font-weight:600}
.sign-box{display:inline-block;width:16px;height:16px;background:#c6e13a}
.info-band{left:55px;top:528px;width:868px;height:105px;background:var(--band);color:#fff;padding:20px 20px 0;font-size:12.8px;line-height:16px}
.info-band .meet{margin-top:14px;font-weight:600;display:flex;align-items:center;gap:14px}
.meet-name{color:var(--bright);font-weight:600;font-size:18px}
.meet-square{width:30px;height:30px;background:#6264a7;border-radius:4px}
.pricing{left:55px;top:665px;width:386px;height:87px;border:1.5px solid var(--ink)}
.pricing-label{left:60px;top:650px;background:#fff;padding:0 5px;color:var(--bright);font-weight:700;font-size:20px;letter-spacing:2px;line-height:24px}
.pricing-title{left:62px;top:680px;font-size:26px;line-height:29px}
.pricing-title b{font-weight:700}
.pricing-amount{left:233px;top:670px;font-family:"Oswald",sans-serif;font-weight:600;font-size:60px;line-height:72px;color:var(--bright)}
.notes{left:55px;top:768px;width:380px;font-size:12.6px;line-height:15px}
.notes p{margin-bottom:15px}
.ask{display:flex;gap:8px}
.ask svg{flex:none}
.ask-left{left:52px;top:958px;width:390px;font-size:12.6px;line-height:15px}
.ask-left b{font-weight:700;font-size:14px}
.accent{color:var(--navy);font-weight:700}
.costs{left:55px;top:1040px;width:386px;border-radius:8px;overflow:hidden;font-size:12.5px;line-height:15px;text-align:center}
.costs-head{background:var(--blue);color:#fff;font-weight:700;letter-spacing:1.5px;font-size:15px;height:30px;line-height:30px}
.costs table{width:100%;border-collapse:collapse}
.costs th{background:var(--pale);font-weight:400;height:70px;border-right:1px solid #fff}
.costs td{background:var(--cell);height:70px;border-right:1px solid #fff}
.costs th:last-child,.costs td:last-child{border-right:0}
.money{font-family:"Oswald",sans-serif;color:var(--blue);font-size:15px;font-weight:500}
.add-label{left:480px;top:656px;color:var(--bright);font-weight:700;font-size:19px;letter-spacing:1.5px}
.rate-box{left:480px;top:700px;width:432px;height:78px;background:var(--blue);border-radius:6px;display:flex;align-items:center;padding-left:16px;gap:14px}
.rate-amount{font-family:"Oswald",sans-serif;font-weight:600;font-size:62px;color:#fff;line-height:1}
.rate-text{color:var(--pale);font-size:26px;line-height:28px;font-weight:500}
.rate-text span{font-weight:400;display:block}
.breathe-pre{left:484px;top:800px;font-size:27px;line-height:32px}
.breathe{left:484px;top:832px;font-weight:800;font-size:37px;line-height:42px;color:var(--blue);letter-spacing:.5px}
.pitch{left:484px;top:888px;width:430px;font-size:15px;line-height:19px;font-weight:500}
.ask-right{left:480px;top:1002px;width:440px;font-size:15px;line-height:19px}
.ask-right b{font-weight:700;font-size:14px}
.cta{left:480px;top:1088px;width:342px;height:42px;background:var(--bright);border-radius:8px;color:#fff;font-weight:800;font-size:28px;letter-spacing:5px;line-height:42px;padding-left:14px}
.contact{left:480px;font-size:18px;display:flex;align-items:center;gap:8px}
.contact-row1{top:1153px}
.contact-row2{top:1192px;letter-spacing:5px}
.contact .sep{color:var(--bright);font-weight:700;margin:0 10px}
.web-mid{color:var(--bright);font-weight:700}
</style>
</head>
<body>
<main class="flyer">
  <svg class="hero-art" viewBox="0 0 979 530" aria-hidden="false">
    <polygon points="380,0 979,0 979,518 488,518" fill="#dfe2e6" role="img" aria-label="Photo of a surprised woman holding a phone and a fan of banknotes, with bills flying around her"/>
    <polygon points="362,0 378,0 498,470 482,470" fill="var(--bright)"/>
    <rect x="620" y="514" width="359" height="12" fill="var(--bright)"/>
  </svg>

  <div class="abs brand"><span>LedgerMint<br>Corp.</span><span class="brand-dot"></span></div>
  <div class="abs headline-relax">RELAX</div>
  <div class="abs headline-sub">WE’VE GOT YOUR</div>
  <div class="abs headline-main">TAXES COVERED!</div>
  <div class="abs dash"></div>
  <p class="abs intro">Our tax preparers have over <strong>20 years experience</strong> and worked both in public accounting firms as well as specialized tax. Our tax services are virtual, so you don’t have to take the time for a personal visit. We take care of everything and can access all your tax slips from the tax agency website directly into our tax software. All signing is done via <span class="sign-tag"><span class="sign-box"></span>SignPad</span></p>

  <section class="abs info-band">
    <p>You can fill and submit the appropriate forms, along with all your other documents, in our secure client portal. It’s important that we understand your situation and any changes in your situation from the past year.</p>
    <p class="meet">If you have a complex tax situation and would like to discuss it, we can meet in virtually over <span class="meet-name">MeetLine</span><span class="meet-square"></span></p>
  </section>

  <div class="abs pricing"></div>
  <div class="abs pricing-label">PRICING</div>
  <div class="abs pricing-title"><b>PERSONAL</b><br>TAX RETURN</div>
  <div class="abs pricing-amount">$100.00</div>

  <div class="abs notes">
    <p>More complex tax returns will be assessed based on the complexity of the return and you will be advised before we start.</p>
    <p>Did you fall behind in filing your income tax save 20% when you file 3 or more years with us. We can do back to 2012 for filing of tax returns.</p>
    <p>If you expect a refund, the earlier you file the sooner you will receive your refund. Our average turn around time prior to April is a couple of days.</p>
  </div>

  <div class="abs ask ask-left">
    <svg width="34" height="62" viewBox="0 0 34 62"><path d="M4 16 A13 13 0 1 1 20 28 Q16 31 16 38 V44" fill="none" stroke="var(--bright)" stroke-width="2.4"/><circle cx="16" cy="54" r="4" fill="none" stroke="var(--bright)" stroke-width="2.4"/></svg>
    <div><b>How will you feel?</b><br>Calm, relaxed, and able to make good business decisions. And you’ll have more time to work on your business. In short, you’ll be able to <span class="accent">BREATHE EASY</span></div>
  </div>

  <section class="abs costs">
    <div class="costs-head">BOOKKEEPING &amp; ACCOUNTING COSTS</div>
    <table>
      <tr><th>DIY</th><th>Part-Time Bookkeeper</th><th>Full-Time Bookkeeper</th><th>FullOut sources Accounting Team</th></tr>
      <tr><td>No added financial cost</td><td><span class="money">$3,500-4,500</span><br>Per month +<br>benefits<sup>(1)</sup></td><td><span class="money">$4,800-5,500</span><br>Per month +<br>benefits<sup>(2)</sup></td><td><span class="money">$5,000+</span><sup>(3)</sup></td></tr>
    </table>
  </section>

  <div class="abs add-label">ADD A BUSINESS OR RENTAL SCHEDULE</div>
  <div class="abs rate-box"><span class="rate-amount">$125</span><span class="rate-text">PER BUSINESS OR<span>RENTAL PROPERTY</span></span></div>
  <div class="abs breathe-pre">TODAY SO YOU CAN START TO</div>
  <div class="abs breathe">BREATHE EASY</div>
  <p class="abs pitch">Imagine having your bookkeeping on auto pilot, with everything always up to date and available at your fingertips. Anytime. Anywhere. You’ll always know exactly where you stand with your cash flow—how much you have, owe, are owed, and have made.</p>

  <div class="abs ask ask-right">
    <svg width="34" height="62" viewBox="0 0 34 62"><path d="M4 16 A13 13 0 1 1 20 28 Q16 31 16 38 V44" fill="none" stroke="var(--bright)" stroke-width="2.4"/><circle cx="16" cy="54" r="4" fill="none" stroke="var(--bright)" stroke-width="2.4"/></svg>
    <div><b>Sound too good to be true?</b><br>That’s exactly how our clients feel once all their bookkeeping stresses are gone.</div>
  </div>

  <div class="abs cta">CALL US TODAY!</div>
  <div class="abs contact contact-row1">
    <svg width="18" height="18" viewBox="0 0 18 18"><circle cx="9" cy="9" r="8.5" fill="var(--bright)"/><path d="M6 4.5 L7.8 6.6 L6.9 7.7 Q8 10 10.3 11.1 L11.4 10.2 L13.5 12 L12.4 13.4 Q7.5 13 4.6 5.6 Z" fill="#fff"/></svg>
    <span>555 0142 0199</span><span class="sep">|</span>
    <svg width="18" height="18" viewBox="0 0 18 18"><circle cx="9" cy="9" r="8.5" fill="var(--bright)"/><rect x="4.5" y="6" width="9" height="6.5" fill="none" stroke="#fff" stroke-width="1.2"/><path d="M4.5 6 L9 9.8 L13.5 6" fill="none" stroke="#fff" stroke-width="1.2"/></svg>
    <span>info@ledgermintcorp.com</span>
  </div>
  <div class="abs contact contact-row2">
    <svg width="18" height="18" viewBox="0 0 18 18"><circle cx="9" cy="9" r="7.5" fill="none" stroke="var(--bright)" stroke-width="2"/><path d="M1.5 9 H16.5 M9 1.5 Q4 9 9 16.5 Q14 9 9 1.5" fill="none" stroke="var(--bright)" stroke-width="1.4"/></svg>
    <span>www.<span class="web-mid">ledgermintcorp</span>.com</span>
  </div>
</main>
</body>
</html>
```